Roost 'n run. Chicken shop

yDesign special menu with special pictures within 48 h
Very smaple menu

Target Market(s)

Local

Industry/Entity Type

Food

Colors
FFF300
FFF600
FEFA6F
FFFEC7
FFFEE8

Requirements
Must have
• IGood quality picture
Nice to have
• Good quality pictures

```html
<!DOCTYPE html>
<html lang="en">
<head>
<meta charset="utf-8">
<title>Roost 'n run – Menu</title>
<link href="https://fonts.googleapis.com/css2?family=Anton&family=Oswald:wght@400;500;700&display=swap" rel="stylesheet">
<style>
:root{
  --gold:#DDA032;
  --red:#8E1B17;
  --ink:#111111;
  --paper:#FFFFFF;
}
*{margin:0;padding:0;box-sizing:border-box}
html,body{width:1200px;height:1200px;overflow:hidden;background:var(--paper)}
.sheet{position:absolute;left:0;top:212px;width:1200px;height:776px;overflow:hidden;background:var(--paper)}
.menu{position:absolute;left:0;top:0;width:1654px;height:1070px;transform:scale(0.7255);transform-origin:0 0;font-family:'Oswald',sans-serif;color:var(--ink)}
.menu > *{position:absolute;line-height:1}
.photo{border-radius:4px}
.photo-wings{left:0;top:0;width:305px;height:270px;background:radial-gradient(ellipse at 55% 45%,#C4491C 0%,#D8702F 45%,#E9B48A 75%,rgba(255,255,255,0) 100%)}
.photo-tenders{left:0;top:432px;width:310px;height:285px;background:radial-gradient(ellipse at 50% 45%,#D9952F 0%,#E8B45E 50%,#F4DDB5 78%,rgba(255,255,255,0) 100%)}
.photo-burger-top{left:1370px;top:0;width:284px;height:258px;background:radial-gradient(ellipse at 55% 50%,#D9412A 0%,#7DB33A 35%,#D79B52 60%,#EBC992 82%,rgba(255,255,255,0) 100%)}
.photo-burger-bottom{left:1350px;top:553px;width:304px;height:472px;background:radial-gradient(ellipse at 55% 50%,#D2502C 0%,#C9413A 25%,#7FB040 45%,#D6A062 65%,#EDD2A8 85%,rgba(255,255,255,0) 100%)}
.band{background:var(--gold)}
.band-fade{background:linear-gradient(90deg,rgba(221,160,50,0) 0%,var(--gold) 12%)}
.band-title{font-family:'Anton',sans-serif;font-size:40px;color:var(--ink);letter-spacing:.5px}
.band-title .light{font-family:'Oswald',sans-serif;font-weight:400}
.band-note{font-size:16px;color:var(--paper);font-weight:400}
.step{font-size:21px;color:var(--red);font-weight:400}
.step small{font-size:16px}
.item{font-family:'Oswald',sans-serif;font-weight:700;font-size:16px;letter-spacing:.5px}
.size{font-family:'Anton',sans-serif;font-size:23px;letter-spacing:2px}
.sauce-bar{background:var(--gold);height:22px;left:56px;width:723px}
.sauce{font-weight:700;font-size:15px;color:var(--red);letter-spacing:.5px}
.logo{font-family:'Anton',sans-serif;font-size:80px;color:var(--ink);letter-spacing:1px;left:560px;top:42px;width:534px;text-align:center}
.dish{font-family:'Anton',sans-serif;font-size:24px;color:var(--red);letter-spacing:.5px}
.desc{font-size:16px;line-height:1.28;font-weight:400}
.vbar{background:var(--gold);top:775px;width:80px;height:295px}
.vtext{font-family:'Anton',sans-serif;color:var(--paper);transform:rotate(-90deg);transform-origin:0 0;white-space:nowrap}
.side{font-weight:700;font-size:12px;color:var(--red);letter-spacing:.8px}
.tiny{font-size:10.5px;line-height:1.25;font-weight:400}
.tiny b{color:var(--red);font-weight:700;font-size:11.5px}
.fry{font-weight:700;font-size:12px;color:var(--red);letter-spacing:.5px}
</style>
</head>
<body>
<div class="sheet">
<main class="menu">

  <div class="photo photo-wings" role="img" aria-label="Photo of breaded chicken wings with a dip"></div>
  <div class="photo photo-tenders" role="img" aria-label="Photo of buttermilk fried chicken tenders"></div>
  <div class="photo photo-burger-top" role="img" aria-label="Photo of a chicken burger with cheese, tomato and lettuce"></div>
  <div class="photo photo-burger-bottom" role="img" aria-label="Photo of a sesame bun chicken burger with tomato and lettuce"></div>

  <h1 class="logo">ROOST 'N RUN</h1>

  <!-- Breaded wings -->
  <div class="band band-fade" style="left:290px;top:136px;width:351px;height:80px"></div>
  <h2 class="band-title" style="left:321px;top:146px">BREADED WINGS</h2>
  <p class="band-note" style="left:321px;top:187px">All Wings served with Fries and one dip</p>

  <p class="step" style="left:61px;top:248px">STEP 1</p>
  <p class="size" style="left:61px;top:275px">WINGS</p>
  <p class="size" style="left:61px;top:306px">BONELESS</p>

  <p class="step" style="left:204px;top:248px">STEP 2</p>
  <p class="item" style="left:204px;top:275px;line-height:1.5">4 WINGS<br>8 WINGS<br>10 WINGS<br>12 WINGS</p>
  <p class="item" style="left:325px;top:275px;line-height:1.5">6.99<br>9.75<br>11.50<br>12.95</p>

  <p class="step" style="left:400px;top:248px">STEP 3. <small>Choose your flavour</small></p>
  <p class="item" style="left:400px;top:275px;line-height:1.5">1 ORIGINAL<br>2 BUFFALO<br>3 BBQ<br>4 LEMON PAPER</p>
  <p class="item" style="left:590px;top:275px;line-height:1.5">5 GARLIC PARMESAN<br>6 DYNAMITE<br>7 NASHVILLE OH HOT DAMN</p>

  <p class="step" style="left:333px;top:382px">STEP 4. <small>Choose your sauce</small></p>
  <div class="sauce-bar" style="top:408px"></div>
  <p class="sauce" style="left:61px;top:411px">BLUEE CHEESE</p>
  <p class="sauce" style="left:228px;top:411px">HONEY MUSTARD</p>
  <p class="sauce" style="left:437px;top:411px">HOUSE RANCH</p>
  <p class="sauce" style="left:599px;top:411px">ROOST 'N RUN SPECIAL</p>

  <!-- Tenders -->
  <div class="band band-fade" style="left:296px;top:463px;width:483px;height:80px"></div>
  <h2 class="band-title" style="left:330px;top:474px;font-size:32px;letter-spacing:0">BUTTERMILK MARINATED TENDERS</h2>
  <p class="band-note" style="left:330px;top:507px">All Tenders served with Fries and one dip</p>

  <p class="step" style="left:246px;top:566px">STEP 1</p>
  <p class="size" style="left:246px;top:594px">LARGE</p>
  <p class="size" style="left:246px;top:624px">MINI</p>

  <p class="step" style="left:338px;top:566px">STEP 2</p>
  <p class="item" style="left:338px;top:594px;line-height:1.5">3 TENDERS<br>6 TENDERS</p>
  <p class="item" style="left:431px;top:594px;line-height:1.5">5.99<br>8.99</p>

  <p class="step" style="left:481px;top:566px">STEP 3. <small>Choose your flavour</small></p>
  <p class="item" style="left:481px;top:594px;line-height:1.5">1 ORIGINAL<br>2 BUFFALO<br>3 BBQ<br>4 LEMON PAPER</p>
  <p class="item" style="left:602px;top:594px;line-height:1.5">5 GARLIC PARMESAN<br>6 DYNAMITE<br>7 NASHVILLE OH HOT DAMN</p>

  <p class="step" style="left:333px;top:695px">STEP 4. <small>Choose your sauce</small></p>
  <div class="sauce-bar" style="top:720px"></div>
  <p class="sauce" style="left:61px;top:723px">BLUEE CHEESE</p>
  <p class="sauce" style="left:228px;top:723px">HONEY MUSTARD</p>
  <p class="sauce" style="left:437px;top:723px">HOUSE RANCH</p>
  <p class="sauce" style="left:599px;top:723px">ROOST 'N RUN SPECIAL</p>

  <!-- Sides -->
  <div class="vbar" style="left:24px"></div>
  <p class="vtext" style="left:38px;top:1032px;font-size:66px">SIDES</p>
  <p class="side" style="left:110px;top:781px">1 - CHICKEN POP CORN</p>
  <p class="side" style="left:304px;top:781px">5.50</p>
  <p class="tiny" style="left:110px;top:803px;width:195px">Chicken pop corn topped with meltd cheddar cheese , dynamite sause , sismes</p>
  <p class="side" style="left:110px;top:846px">2 - CHILI CHEESE BITES</p>
  <p class="tiny" style="left:110px;top:869px">Chili cheese bites, select your dip</p>
  <p class="side" style="left:110px;top:900px">3 - MOZERLA STICK</p>
  <p class="side" style="left:110px;top:929px">4 - HALOMI STICK</p>
  <p class="side" style="left:110px;top:958px">5 - GARLIC MUSHROOMS BITES</p>
  <p class="side" style="left:110px;top:988px">6 - ONION RINGS</p>
  <p class="tiny" style="left:110px;top:1011px;width:190px">Roost 'n run special (mashed potato, grave sauce, honey mustard slaw</p>

  <!-- Loaded fries -->
  <div class="vbar" style="left:339px"></div>
  <p class="vtext" style="left:341px;top:1055px;font-size:30px">LOADED</p>
  <p class="vtext" style="left:368px;top:975px;font-size:54px">FRIES</p>
  <p class="tiny" style="left:424px;top:783px"><b>FRY BY</b> Chips loaded with melted cheese , daynmite sause , jalapeño</p>
  <p class="tiny" style="left:424px;top:806px"><b>TAKES LOADED</b> Chips load3d with melted cheese, hot sause , rolled chips</p>
  <p class="tiny" style="left:424px;top:830px"><b>CHICKETOOS</b> Chips tenders loaded with melt3d cheese , ketchup, cheese puffs</p>
  <p class="tiny" style="left:424px;top:853px;width:360px"><b>OH HOT DAMN</b> Chips nashville tender , melted cheese , sarcha sause , green chilli paper</p>
  <p class="tiny" style="left:424px;top:888px;width:360px"><b>POP CORN</b><br>1 - Chips Chicken pop corn , melted cheese , Daynmaited sause , Sesame<br>2 - Chips , tenders , montero jack cheese, crispy Fried onion , roost dressing</p>
  <p class="fry" style="left:424px;top:956px;line-height:1.8">Seaoned FRIES<br>Regular Sweet Potato<br>Haloomi FRIES</p>
  <p class="fry" style="left:613px;top:956px;line-height:1.8">Regular FRIES<br>Cajuan FRIES</p>

  <!-- Sandwich option 1 -->
  <div class="band" style="left:1015px;top:136px;width:376px;height:80px"></div>
  <h2 class="band-title" style="left:1028px;top:147px">SANDWICH <span class="light">OPTION 1</span></h2>
  <p class="band-note" style="left:1028px;top:189px">All meals served with chips and dip</p>

  <p class="dish" style="left:873px;top:259px">1 - CLASSIC BURGER</p>
  <p class="dish" style="left:1184px;top:259px">5.50</p>
  <p class="desc" style="left:873px;top:295px;width:290px">Fried chicken breast, fresh pickles and creamy mayo in a soft brioche bun</p>

  <p class="dish" style="left:873px;top:361px">2 - ROOST 'N RUN SPECIAL</p>
  <p class="dish" style="left:1184px;top:361px">6.95</p>
  <p class="desc" style="left:873px;top:396px;width:300px">Relish sauce, Fried chicken breast, Honey mustard, Red cabbage in a soft brioche bun</p>

  <p class="dish" style="left:873px;top:459px">3 - NASHVILLE OH HOT DAMN</p>
  <p class="dish" style="left:1184px;top:459px">7.99</p>
  <p class="desc" style="left:873px;top:494px;width:310px">Fried nashville chicken breast, fresh pickles and roost 'n run sauce, pot of grace and mashed potato</p>

  <p class="dish" style="left:1272px;top:259px">4 - DOUBLE CHEESY TOASTED</p>
  <p class="dish" style="left:1584px;top:259px">5.99</p>
  <p class="desc" style="left:1272px;top:295px">Tenders, Cheese, Slaw, Pickles, Mayo</p>

  <p class="dish" style="left:1272px;top:361px">5 - DYNAMITE BURGER</p>
  <p class="dish" style="left:1584px;top:361px">6.50</p>
  <p class="desc" style="left:1272px;top:396px;width:300px">Sweet mayo, Iceberg lettuce, Fried chicken breast, Dynamite sauce, soft deli rolls</p>

  <p class="dish" style="left:1272px;top:465px">6 - MINI FILLET SLIDER</p>
  <p class="dish" style="left:1584px;top:465px">4.99</p>
  <p class="desc" style="left:1272px;top:500px;width:300px">Lemon herbs, Demled peri-peri, Mango lime Mini fellet, lettuce, Cheese, select your flavours in a mini bun</p>

  <!-- Sandwich option 2 -->
  <div class="band" style="left:1015px;top:618px;width:376px;height:80px"></div>
  <h2 class="band-title" style="left:1028px;top:629px">SANDWICH <span class="light">OPTION 2</span></h2>
  <p class="band-note" style="left:1028px;top:671px">All meals served with chips and dip</p>

  <p class="step" style="left:881px;top:732px">STEP 1</p>
  <p class="item" style="left:881px;top:760px">Select your base</p>
  <p class="item" style="left:1020px;top:760px">2.50</p>

  <p class="step" style="left:1150px;top:732px">STEP 2</p>
  <p class="item" style="left:1150px;top:760px">Select your chicken</p>
  <p class="item" style="left:1314px;top:760px">3.50</p>
  <p class="desc" style="left:1150px;top:779px;font-size:12px">Tenders, Chicken breast</p>

  <p class="step" style="left:881px;top:820px">STEP 3. <small>Choose your favorite sauce</small></p>
  <p class="item" style="left:881px;top:848px;font-size:14px;line-height:1.69">1 CLASSIC<br>2 BUFFALO<br>3 BBQ<br>4 MANGO LIME<br>5 DYNAMITE<br>6 LEMON HERBS<br>7 NASHVILLE<br>8 DEMLESS PERI-PERI</p>

  <p class="step" style="left:1150px;top:820px">STEP 4. <small>Add topping</small></p>
  <p class="item" style="left:1150px;top:848px;font-size:14px;line-height:1.69">CHEESE<br>LETTUCE</p>
  <p class="item" style="left:1284px;top:848px;font-size:14px;line-height:1.69">SLAW<br>PICKLES</p>

  <p class="step" style="left:1150px;top:914px">STEP 5. <small>Select your sauce</small></p>
  <p class="item" style="left:1150px;top:942px;font-size:14px;line-height:1.69">BLUEE CHEESE<br>HONEY MUSTARD<br>HOUSE RANCH</p>
  <p class="item" style="left:1269px;top:942px;font-size:14px;line-height:1.69">DAYNMAITED<br>ROOST 'N RUN SPECIAL</p>

</main>
</div>
</body>
</html>
```